UI Redesign For Mobile Events iPhone App

We need a new UI design for our Social Events mobile app. Our app called Zirvo is geared to help users find trending events in their local area. We show visual metrics on percent full and male female ratio and age group ratings. We want people to see whats going on at event before they get there through our app. Also we have a group chat portion to our app that we need included in the design. We would like to see a fresh, clean, and easy to use user interface that uses colors like, purple, blue and or hot pink.You may visit our website myzirvo.example for more information about what our app is geared to do.

Target Market(s)

Our target market people that use social networks and attend social events ranging from ages 16-44.

Industry/Entity Type

Events

Requirements
Must have
• We would like to see an Example layout of all screens. (UPDATE: Please use our current background in your design, A PSD has been uploaded for you to grab the background. The Zirvo Logo is NOT required to be included at the top of every screen)

-Profile Screen: Shows points earned, events attending, events created
-Event Listings Screen: Must have large image for event, visual metrics, date& time, location, attend button, invite friends button, Label for user who created the event
-Event Description Page: Shows everything as the event listing, has a description of the event, shows friends that are attending, points available
-Group Messaging Screen
-Slide Out Navigation Screen
-Notification Screen
-Ticket Screen
-Friends Activity Screen
-Friends Profile View: Shows events they've attended and points they've earned under their contact picture; invite button
-Sign-In Screen
-Register Screen

A way to label/categorize our different types of events:
-Nightlife
-Family
-Live Music & Concerts
-Restaurants
Group Chat Layout
Visual Meters for Percent Full, Male Female Ratio, Age Rating

```html
<!DOCTYPE html>
<html lang="en">
<head>
<meta charset="utf-8">
<title>Zirvo App Design 2</title>
<link rel="stylesheet" href="https://fonts.googleapis.com/css2?family=Heebo:wght@100;300;400;500&family=Roboto+Condensed:wght@400;500&display=swap">
<style>
  :root{
    --board-light:#f5f0f0;
    --board-edge:#e4d6d9;
    --ribbon:#f0173f;
    --ink:#1b1b1b;
    --status:#000;
    --menu-bg:#1b0f1e;
    --menu-line:#2c2030;
    --menu-active:#5b1f95;
    --menu-text:#d9d2dc;
    --card:#ffffff;
    --card-footer:#f4f4f6;
    --title-navy:#1c1690;
    --price:#e4202e;
    --tag:#f5b400;
    --join:#4a1c8c;
    --muted:#777;
    --ring-track:#dddddd;
    --ring-fill:#f48a12;
    --ratio-blue:#2a2cff;
    --ratio-pink:#ff1f8f;
    --ratio-label:#2a2cc8;
  }
  *{box-sizing:border-box;margin:0;padding:0}
  html,body{width:1200px;height:1000px;overflow:hidden}
  body{
    position:relative;
    font-family:"Heebo",sans-serif;
    color:var(--ink);
    background:radial-gradient(ellipse at 50% 40%,var(--board-light) 0%,var(--board-light) 40%,var(--board-edge) 100%);
  }
  .ribbon{position:absolute;left:0;top:0;width:170px;height:150px}
  .board-title{position:absolute;left:360px;top:58px;display:flex;align-items:baseline;gap:18px;white-space:nowrap}
  .board-title__brand{font-weight:100;font-size:72px;letter-spacing:1px;line-height:1}
  .board-title__sub{font-weight:400;font-size:40px;line-height:1}

  .screen{position:absolute;top:220px;width:322px;height:570px;overflow:hidden;background:#000}
  .screen--menu{left:36px}
  .screen--original{left:439px}
  .screen--blur{left:838px}
  .screen-label{position:absolute;top:836px;font-weight:300;font-size:33px;white-space:nowrap}

  .app-bg{position:absolute;inset:0;
    background:
      radial-gradient(circle at 60% 12%,rgba(230,120,230,.75) 0%,rgba(120,60,200,0) 30%),
      radial-gradient(circle at 85% 45%,rgba(60,200,240,.8) 0%,rgba(40,90,200,0) 35%),
      radial-gradient(circle at 20% 40%,rgba(70,120,220,.55) 0%,rgba(0,0,0,0) 40%),
      linear-gradient(180deg,#151842 0%,#1c2a6a 35%,#0d1030 70%,#050510 100%);}
  .app-bg--blur{filter:blur(0);background:
      radial-gradient(circle at 60% 12%,rgba(220,130,230,.6) 0%,rgba(120,60,200,0) 38%),
      radial-gradient(circle at 85% 45%,rgba(80,190,235,.6) 0%,rgba(40,90,200,0) 42%),
      linear-gradient(180deg,#1b1f4e 0%,#243274 40%,#121638 75%,#07071a 100%);}

  .status{position:absolute;left:0;top:0;width:100%;height:20px;background:var(--status);color:#fff;font-size:11px;font-weight:500;display:flex;align-items:center;justify-content:space-between;padding:0 6px;z-index:5}
  .status__left,.status__right{display:flex;align-items:center;gap:4px}
  .status__time{position:absolute;left:50%;transform:translateX(-50%)}

  .app{position:absolute;top:0;left:0;width:322px;height:570px}
  .app--shifted{left:182px}
  .app-header{position:absolute;top:20px;left:0;width:100%;height:52px;color:#fff}
  .app-header__menu{position:absolute;left:10px;top:17px}
  .app-header__title{position:absolute;left:0;right:0;top:9px;text-align:center;font-weight:300;font-size:31px}
  .app-header__add{position:absolute;right:10px;top:12px}

  .featured-tag{position:absolute;left:10px;top:73px;height:15px;width:72px;background:var(--tag);color:#fff;font-size:7px;display:flex;align-items:center;gap:4px;padding-left:4px;clip-path:polygon(0 0,86% 0,100% 100%,0 100%)}
  .event-card{position:absolute;left:10px;width:302px}
  .event-card__head{position:relative;height:43px;background:var(--card);padding:2px 0 0 3px}
  .event-card__title{font-family:"Roboto Condensed",sans-serif;font-size:15px;color:var(--title-navy);line-height:16px;white-space:nowrap}
  .event-card__place{font-size:11px;line-height:13px;white-space:nowrap}
  .event-card__date{font-size:8px;line-height:10px}
  .event-card__price{position:absolute;right:0;top:0;width:44px;height:100%;border-left:1px solid #ddd;background:var(--card);color:var(--price);font-size:11px;text-align:center;padding-top:9px}
  .event-card__photo{height:127px}
  .photo--festival{background:linear-gradient(100deg,#6f8b57 0%,#8fb0c8 30%,#d6a22a 55%,#e5341e 75%,#c71e2a 100%)}
  .photo--plaza{background:linear-gradient(180deg,#9ab6d6 0%,#c6d6e6 35%,#4d7a40 60%,#6b6f6a 85%,#5a6a45 100%)}
  .event-card__foot{position:relative;height:30px;margin-top:1px;background:var(--card-footer)}
  .join{position:absolute;left:4px;top:3px;display:flex;align-items:center;gap:3px;font-size:8px;color:var(--join)}
  .friends{position:absolute;left:4px;top:16px;display:flex;align-items:center;gap:2px;font-size:7px;color:var(--muted);white-space:nowrap}
  .friends__face{width:12px;height:12px}
  .friends__face--a{background:#b6865a}.friends__face--b{background:#7a5b8c}.friends__face--c{background:#4a6a8a}.friends__face--d{background:#d8b890}
  .friends__text{margin-left:3px}
  .fill-meter{position:absolute;left:168px;top:3px}
  .ratio{position:absolute;right:4px;top:3px;display:flex;align-items:center;gap:6px;font-size:10px;color:var(--ratio-label)}

  .side-menu{position:absolute;left:0;top:20px;width:182px;height:550px;background:var(--menu-bg);z-index:3}
  .side-menu__item{height:57px;display:flex;align-items:center;gap:18px;padding-left:17px;border-bottom:1px solid var(--menu-line);color:var(--menu-text);font-weight:300;font-size:15px}
  .side-menu__item--active{background:var(--menu-active);color:#fff}
  .side-menu__icon{width:24px;height:24px;flex:none}
</style>
</head>
<body>

<svg class="ribbon" viewBox="0 0 170 150" aria-hidden="false">
  <polygon points="0,0 170,0 0,150" fill="var(--ribbon)"/>
  <text x="62" y="66" transform="rotate(-41.4 62 66)" text-anchor="middle" fill="#fff" font-family="Heebo, sans-serif" font-size="30" font-weight="400">REVISED</text>
</svg>

<h1 class="board-title"><span class="board-title__brand">ZIRVO</span><span class="board-title__sub">App Design 2</span></h1>

<!-- Screen: side menu -->
<section class="screen screen--menu">
  <div class="app-bg" role="img" aria-label="App background: dark blue and purple glowing light photo"></div>
  <div class="status"><span class="status__left">●●●○○ VOLT</span><span class="status__time">4:21 PM</span><span class="status__right">✱ 100% <svg width="20" height="9"><rect x=".5" y=".5" width="17" height="8" fill="none" stroke="#fff"/><rect x="2" y="2" width="14" height="5" fill="#fff"/><rect x="18" y="3" width="2" height="3" fill="#fff"/></svg></span></div>
  <div class="app app--shifted">
    <header class="app-header">
      <svg class="app-header__menu" width="26" height="18"><g stroke="#fff" stroke-width="2"><line x1="0" y1="1" x2="26" y2="1"/><line x1="0" y1="9" x2="26" y2="9"/><line x1="0" y1="17" x2="26" y2="17"/></g></svg>
      <div class="app-header__title">Events</div>
    </header>
    <div class="featured-tag"><svg width="8" height="8" viewBox="0 0 10 10"><polygon points="5,0 6.2,3.6 10,3.6 7,5.9 8.1,9.6 5,7.4 1.9,9.6 3,5.9 0,3.6 3.8,3.6" fill="#fff"/></svg>FEATURED</div>
    <article class="event-card" style="top:89px">
      <div class="event-card__head">
        <div class="event-card__title">SOLANA FESTIVAL 2014</div>
        <div class="event-card__place">Bayview City, Philippines</div>
        <div class="event-card__date">Friday, 10Jan @ 8:0 AM</div>
      </div>
      <div class="event-card__photo photo--festival" role="img" aria-label="Event photo: street festival dancers in bright costumes"></div>
      <div class="event-card__foot">
        <div class="join"><svg width="9" height="8" viewBox="0 0 10 9"><path d="M5 9 0 4C-1 1 3-1 5 2 7-1 11 1 10 4Z" fill="var(--join)"/></svg>Unjoin</div>
        <div class="friends"><span class="friends__face friends__face--a" role="img" aria-label="Friend photo"></span><span class="friends__face friends__face--b" role="img" aria-label="Friend photo"></span><span class="friends__face friends__face--c" role="img" aria-label="Friend photo"></span><span class="friends__text">You, Mira &amp; Jonah are joining</span></div>
      </div>
    </article>
    <article class="event-card" style="top:312px">
      <div class="event-card__head">
        <div class="event-card__title">METRO PLAZA SUMMER WORKSHOP</div>
        <div class="event-card__place">Riverside City, Philippines</div>
        <div class="event-card__date">Tuesday, 01April @ 8:0 AM</div>
      </div>
      <div class="event-card__photo photo--plaza" role="img" aria-label="Event photo: shopping plaza beside a tree-lined road"></div>
      <div class="event-card__foot">
        <div class="join"><svg width="9" height="8" viewBox="0 0 10 9"><path d="M5 9 0 4C-1 1 3-1 5 2 7-1 11 1 10 4Z" fill="#888"/></svg>Join</div>
        <div class="friends"><span class="friends__face friends__face--d" role="img" aria-label="Friend photo"></span><span class="friends__text">Tessa is joining</span></div>
      </div>
    </article>
    <article class="event-card" style="top:535px">
      <div class="event-card__head">
        <div class="event-card__title">SUMMER PHOTOGRAPHY CONTEST</div>
        <div class="event-card__place">Hillcrest, Valewood, Philippines</div>
      </div>
    </article>
  </div>
  <nav class="side-menu">
    <div class="side-menu__item"><svg class="side-menu__icon" viewBox="0 0 24 24" fill="none" stroke="#d9d2dc" stroke-width="1.3"><circle cx="8" cy="7" r="3.5"/><circle cx="16" cy="8" r="3"/><path d="M2 20c0-5 12-5 12 0zM13 19c1-4 9-4 9 0z"/></svg>Profile</div>
    <div class="side-menu__item"><svg class="side-menu__icon" viewBox="0 0 24 24" fill="none" stroke="#d9d2dc" stroke-width="1.3"><rect x="2" y="5" width="20" height="14"/><path d="M2 5l10 8 10-8"/></svg>Messages</div>
    <div class="side-menu__item"><svg class="side-menu__icon" viewBox="0 0 24 24" fill="none" stroke="#d9d2dc" stroke-width="1.3"><path d="M5 18V11a7 7 0 0 1 14 0v7l2 2H3z"/><path d="M10 21a2 2 0 0 0 4 0"/></svg>Notifications</div>
    <div class="side-menu__item"><svg class="side-menu__icon" viewBox="0 0 24 24" fill="none" stroke="#d9d2dc" stroke-width="1.3"><circle cx="12" cy="12" r="8"/></svg>My Zirvo</div>
    <div class="side-menu__item"><svg class="side-menu__icon" viewBox="0 0 24 24" fill="none" stroke="#d9d2dc" stroke-width="1.3"><path d="M13 3h8v8L11 21 3 13z"/><circle cx="17" cy="7" r="1.4"/></svg>Tickets</div>
    <div class="side-menu__item side-menu__item--active"><svg class="side-menu__icon" viewBox="0 0 24 24" fill="none" stroke="#fff" stroke-width="1.3"><circle cx="12" cy="12" r="3"/><circle cx="12" cy="3.5" r="1.5"/><circle cx="12" cy="20.5" r="1.5"/><circle cx="3.5" cy="12" r="1.5"/><circle cx="20.5" cy="12" r="1.5"/><circle cx="6" cy="6" r="1.5"/><circle cx="18" cy="6" r="1.5"/><circle cx="6" cy="18" r="1.5"/><circle cx="18" cy="18" r="1.5"/></svg>Events</div>
  </nav>
</section>
<div class="screen-label" style="left:72px">Side Menu Bar</div>

<!-- Screen: original background -->
<section class="screen screen--original">
  <div class="app-bg" role="img" aria-label="App background: dark blue and purple glowing light photo"></div>
  <div class="status"><span class="status__left">●●●○○ VOLT</span><span class="status__time">4:21 PM</span><span class="status__right">✱ 100% <svg width="20" height="9"><rect x=".5" y=".5" width="17" height="8" fill="none" stroke="#fff"/><rect x="2" y="2" width="14" height="5" fill="#fff"/><rect x="18" y="3" width="2" height="3" fill="#fff"/></svg></span></div>
  <div class="app">
    <header class="app-header">
      <svg class="app-header__menu" width="26" height="18"><g stroke="#fff" stroke-width="2"><line x1="0" y1="1" x2="26" y2="1"/><line x1="0" y1="9" x2="26" y2="9"/><line x1="0" y1="17" x2="26" y2="17"/></g></svg>
      <div class="app-header__title">Events</div>
      <svg class="app-header__add" width="26" height="26"><g stroke="#fff" stroke-width="2"><line x1="13" y1="0" x2="13" y2="26"/><line x1="0" y1="13" x2="26" y2="13"/></g></svg>
    </header>
    <div class="featured-tag"><svg width="8" height="8" viewBox="0 0 10 10"><polygon points="5,0 6.2,3.6 10,3.6 7,5.9 8.1,9.6 5,7.4 1.9,9.6 3,5.9 0,3.6 3.8,3.6" fill="#fff"/></svg>FEATURED</div>
    <article class="event-card" style="top:89px">
      <div class="event-card__head">
        <div class="event-card__title">SOLANA FESTIVAL 2014</div>
        <div class="event-card__place">Bayview City, Philippines</div>
        <div class="event-card__date">Friday, 10Jan @ 8:0 AM</div>
        <div class="event-card__price">Free</div>
      </div>
      <div class="event-card__photo photo--festival" role="img" aria-label="Event photo: street festival dancers in bright costumes"></div>
      <div class="event-card__foot">
        <div class="join"><svg width="9" height="8" viewBox="0 0 10 9"><path d="M5 9 0 4C-1 1 3-1 5 2 7-1 11 1 10 4Z" fill="var(--join)"/></svg>Unjoin</div>
        <div class="friends"><span class="friends__face friends__face--a" role="img" aria-label="Friend photo"></span><span class="friends__face friends__face--b" role="img" aria-label="Friend photo"></span><span class="friends__face friends__face--c" role="img" aria-label="Friend photo"></span><span class="friends__text">You, Mira &amp; Jonah are joining</span></div>
        <svg class="fill-meter" width="26" height="26" viewBox="0 0 26 26"><circle cx="13" cy="13" r="10.5" fill="none" stroke="var(--ring-track)" stroke-width="2.5"/><circle cx="13" cy="13" r="10.5" fill="none" stroke="var(--ring-fill)" stroke-width="2.5" stroke-dasharray="49.5 66" transform="rotate(-90 13 13)"/><text x="13" y="15.5" text-anchor="middle" font-size="6.5" font-family="Heebo, sans-serif">75%</text></svg>
        <div class="ratio">M/F Ratio<svg width="24" height="24"><path d="M12 0a12 12 0 0 0 0 24z" fill="var(--ratio-blue)"/><path d="M12 0a12 12 0 0 1 0 24z" fill="var(--ratio-pink)"/></svg></div>
      </div>
    </article>
    <article class="event-card" style="top:312px">
      <div class="event-card__head">
        <div class="event-card__title">METRO PLAZA SUMMER WORKSHOP</div>
        <div class="event-card__place">Riverside City, Philippines</div>
        <div class="event-card__date">Tuesday, 01April @ 8:0 AM</div>
        <div class="event-card__price">$20</div>
      </div>
      <div class="event-card__photo photo--plaza" role="img" aria-label="Event photo: shopping plaza beside a tree-lined road"></div>
      <div class="event-card__foot">
        <div class="join"><svg width="9" height="8" viewBox="0 0 10 9"><path d="M5 9 0 4C-1 1 3-1 5 2 7-1 11 1 10 4Z" fill="#888"/></svg>Join</div>
        <div class="friends"><span class="friends__face friends__face--d" role="img" aria-label="Friend photo"></span><span class="friends__text">Tessa is joining</span></div>
        <svg class="fill-meter" width="26" height="26" viewBox="0 0 26 26"><circle cx="13" cy="13" r="10.5" fill="none" stroke="var(--ring-track)" stroke-width="2.5"/><circle cx="13" cy="13" r="10.5" fill="none" stroke="var(--ring-fill)" stroke-width="2.5" stroke-dasharray="49.5 66" transform="rotate(-90 13 13)"/><text x="13" y="15.5" text-anchor="middle" font-size="6.5" font-family="Heebo, sans-serif">75%</text></svg>
        <div class="ratio">M/F Ratio<svg width="24" height="24"><path d="M12 0a12 12 0 0 0 0 24z" fill="var(--ratio-blue)"/><path d="M12 0a12 12 0 0 1 0 24z" fill="var(--ratio-pink)"/></svg></div>
      </div>
    </article>
    <article class="event-card" style="top:535px">
      <div class="event-card__head">
        <div class="event-card__title">SUMMER PHOTOGRAPHY CONTEST</div>
        <div class="event-card__place">Hillcrest, Valewood, Philippines</div>
        <div class="event-card__price">$25</div>
      </div>
    </article>
  </div>
</section>
<div class="screen-label" style="left:500px">Original BG</div>

<!-- Screen: blurred background -->
<section class="screen screen--blur">
  <div class="app-bg app-bg--blur" role="img" aria-label="App background: softly blurred blue and purple glow"></div>
  <div class="status"><span class="status__left">●●●○○ VOLT</span><span class="status__time">4:21 PM</span><span class="status__right">✱ 100% <svg width="20" height="9"><rect x=".5" y=".5" width="17" height="8" fill="none" stroke="#fff"/><rect x="2" y="2" width="14" height="5" fill="#fff"/><rect x="18" y="3" width="2" height="3" fill="#fff"/></svg></span></div>
  <div class="app">
    <header class="app-header">
      <svg class="app-header__menu" width="26" height="18"><g stroke="#fff" stroke-width="2"><line x1="0" y1="1" x2="26" y2="1"/><line x1="0" y1="9" x2="26" y2="9"/><line x1="0" y1="17" x2="26" y2="17"/></g></svg>
      <div class="app-header__title">Events</div>
      <svg class="app-header__add" width="26" height="26"><g stroke="#fff" stroke-width="2"><line x1="13" y1="0" x2="13" y2="26"/><line x1="0" y1="13" x2="26" y2="13"/></g></svg>
    </header>
    <div class="featured-tag"><svg width="8" height="8" viewBox="0 0 10 10"><polygon points="5,0 6.2,3.6 10,3.6 7,5.9 8.1,9.6 5,7.4 1.9,9.6 3,5.9 0,3.6 3.8,3.6" fill="#fff"/></svg>FEATURED</div>
    <article class="event-card" style="top:89px">
      <div class="event-card__head">
        <div class="event-card__title">SOLANA FESTIVAL 2014</div>
        <div class="event-card__place">Bayview City, Philippines</div>
        <div class="event-card__date">Friday, 10Jan @ 8:0 AM</div>
        <div class="event-card__price">Free</div>
      </div>
      <div class="event-card__photo photo--festival" role="img" aria-label="Event photo: street festival dancers in bright costumes"></div>
      <div class="event-card__foot">
        <div class="join"><svg width="9" height="8" viewBox="0 0 10 9"><path d="M5 9 0 4C-1 1 3-1 5 2 7-1 11 1 10 4Z" fill="var(--join)"/></svg>Unjoin</div>
        <div class="friends"><span class="friends__face friends__face--a" role="img" aria-label="Friend photo"></span><span class="friends__face friends__face--b" role="img" aria-label="Friend photo"></span><span class="friends__face friends__face--c" role="img" aria-label="Friend photo"></span><span class="friends__text">You, Mira &amp; Jonah are joining</span></div>
        <svg class="fill-meter" width="26" height="26" viewBox="0 0 26 26"><circle cx="13" cy="13" r="10.5" fill="none" stroke="var(--ring-track)" stroke-width="2.5"/><circle cx="13" cy="13" r="10.5" fill="none" stroke="var(--ring-fill)" stroke-width="2.5" stroke-dasharray="49.5 66" transform="rotate(-90 13 13)"/><text x="13" y="15.5" text-anchor="middle" font-size="6.5" font-family="Heebo, sans-serif">75%</text></svg>
        <div class="ratio">M/F Ratio<svg width="24" height="24"><path d="M12 0a12 12 0 0 0 0 24z" fill="var(--ratio-blue)"/><path d="M12 0a12 12 0 0 1 0 24z" fill="var(--ratio-pink)"/></svg></div>
      </div>
    </article>
    <article class="event-card" style="top:312px">
      <div class="event-card__head">
        <div class="event-card__title">METRO PLAZA SUMMER WORKSHOP</div>
        <div class="event-card__place">Riverside City, Philippines</div>
        <div class="event-card__date">Tuesday, 01April @ 8:0 AM</div>
        <div class="event-card__price">$20</div>
      </div>
      <div class="event-card__photo photo--plaza" role="img" aria-label="Event photo: shopping plaza beside a tree-lined road"></div>
      <div class="event-card__foot">
        <div class="join"><svg width="9" height="8" viewBox="0 0 10 9"><path d="M5 9 0 4C-1 1 3-1 5 2 7-1 11 1 10 4Z" fill="#888"/></svg>Join</div>
        <div class="friends"><span class="friends__face friends__face--d" role="img" aria-label="Friend photo"></span><span class="friends__text">Tessa is joining</span></div>
        <svg class="fill-meter" width="26" height="26" viewBox="0 0 26 26"><circle cx="13" cy="13" r="10.5" fill="none" stroke="var(--ring-track)" stroke-width="2.5"/><circle cx="13" cy="13" r="10.5" fill="none" stroke="var(--ring-fill)" stroke-width="2.5" stroke-dasharray="49.5 66" transform="rotate(-90 13 13)"/><text x="13" y="15.5" text-anchor="middle" font-size="6.5" font-family="Heebo, sans-serif">75%</text></svg>
        <div class="ratio">M/F Ratio<svg width="24" height="24"><path d="M12 0a12 12 0 0 0 0 24z" fill="var(--ratio-blue)"/><path d="M12 0a12 12 0 0 1 0 24z" fill="var(--ratio-pink)"/></svg></div>
      </div>
    </article>
    <article class="event-card" style="top:535px">
      <div class="event-card__head">
        <div class="event-card__title">SUMMER PHOTOGRAPHY CONTEST</div>
        <div class="event-card__place">Hillcrest, Valewood, Philippines</div>
        <div class="event-card__price">$25</div>
      </div>
    </article>
  </div>
</section>
<div class="screen-label" style="left:940px">Blur BG</div>

</body>
</html>
```